Teilnehmerzertifikat für Expeditionsmobil
Zielgruppe
Wir bitten alles Rund um das Thema Expeditionsmobil an. Unter anderem unsere Lagerfeuer und Weite Fahrt nach Tunesien und dafür benötige ich ein Teilnehmer Zertifikat.
Aufgabenstellung
Im Hintergrund soll ein Bild von der Sahara verarbeitet sein und im Vordergrund möchte ich von jedem Teilnehmer ein Bild mit dem eigenen Expeditonsfahrzeug einfügen. Das Zertifikat soll persöhnlich und wie von einem Freund sein

```html
<!DOCTYPE html>
<html lang="de">
<head>
<meta charset="utf-8">
<title>Teilnehmerzertifikat Tunesien 2024</title>
<link rel="stylesheet" href="https://fonts.googleapis.com/css2?family=Poppins:ital,wght@1,800;1,900&family=Manrope:wght@500;600;700;800&family=Damion&display=swap">
<style>
  :root {
    --page-bg: #a3a3a3;
    --paper: #ffffff;
    --red: #e8202a;
    --ink: #1d1b1a;
    --sand-light: #f2dcb0;
    --sand-mid: #e2bd82;
    --sand-deep: #c99a5e;
    --photo-ring: #e8202a;
  }
  * { box-sizing: border-box; margin: 0; padding: 0; }
  html, body { width: 1000px; height: 1200px; overflow: hidden; }
  body {
    background: var(--page-bg);
    font-family: "Manrope", sans-serif;
    color: var(--ink);
    position: relative;
  }
  .certificate {
    position: absolute;
    left: 50px; top: 281px;
    width: 900px; height: 637px;
    background: var(--paper);
    box-shadow: 0 18px 40px rgba(0,0,0,0.35);
    overflow: hidden;
  }
  .desert-photo {
    position: absolute; left: 0; top: 0;
    width: 900px; height: 481px;
    background:
      radial-gradient(ellipse 60% 70% at 25% 45%, rgba(70,80,95,0.35), transparent 70%),
      linear-gradient(170deg, var(--sand-light) 0%, var(--sand-mid) 55%, var(--sand-deep) 100%);
  }
  .tour-line {
    position: absolute; right: 40px; top: 38px;
    font-family: "Poppins", sans-serif; font-style: italic; font-weight: 800;
    font-size: 23px; letter-spacing: -0.5px; color: var(--ink);
    text-shadow: 0 0 3px rgba(255,255,255,0.8);
  }
  .tour-title {
    position: absolute; right: 40px; top: 62px;
    font-family: "Poppins", sans-serif; font-style: italic; font-weight: 900;
    font-size: 78px; line-height: 1; letter-spacing: -2px; color: var(--red);
    text-shadow: 2px 2px 0 #fff, -1px -1px 0 #fff, 1px -1px 0 #fff, -1px 1px 0 #fff, 4px 5px 8px rgba(0,0,0,0.3);
  }
  .participant-name {
    position: absolute; left: 400px; width: 452px; top: 150px;
    font-family: "Damion", cursive; font-size: 70px; line-height: 1;
    text-align: center; color: var(--ink);
  }
  .name-rule {
    position: absolute; left: 423px; top: 234px;
    width: 427px; height: 2px; background: var(--ink);
  }
  .tribute-text {
    position: absolute; left: 400px; width: 452px; top: 248px;
    font-size: 13.5px; font-weight: 600; line-height: 18px; text-align: center;
  }
  .thanks-banner {
    position: absolute; left: 405px; top: 357px;
    width: 444px; height: 63px;
    background: var(--red); color: #fff; border-radius: 8px;
    box-shadow: 4px 6px 10px rgba(0,0,0,0.25);
    display: flex; align-items: center; justify-content: center;
    font-size: 16px; font-weight: 700; line-height: 21px; text-align: center;
  }
  .vehicle-photo {
    position: absolute; left: 132px; top: 333px;
    width: 220px; height: 220px;
  }
  .event-date {
    position: absolute; left: 378px; width: 216px; top: 507px;
    font-size: 32px; font-weight: 700; color: var(--red); text-align: center;
  }
  .event-address {
    position: absolute; left: 378px; width: 216px; top: 549px;
    font-size: 13.5px; font-weight: 600; text-align: center;
  }
  .sign-rule {
    position: absolute; top: 574px; height: 1.5px; width: 216px; background: var(--red);
  }
  .sign-rule.place { left: 378px; }
  .sign-rule.signers { left: 617px; }
  .sign-label {
    position: absolute; top: 584px; width: 216px;
    font-size: 15.5px; font-weight: 600; text-align: center;
  }
  .sign-label.place { left: 378px; }
  .sign-label.signers { left: 617px; }
  .brand {
    position: absolute; left: 50px; top: 560px;
    display: flex; align-items: center; gap: 10px;
  }
  .brand-dot { width: 26px; height: 26px; border-radius: 50%; background: var(--red); }
  .brand-name { font-size: 22px; font-weight: 800; color: var(--red); }
</style>
</head>
<body>
  <main class="certificate">
    <div class="desert-photo" role="img" aria-label="Saharadünen mit einem blauen Expeditionsmobil im Sand"></div>

    <p class="tour-line">SCHRIFTZUG LAGERFEUER UND WEITE FAHRT</p>
    <h1 class="tour-title">TUNESIEN 2024</h1>

    <p class="participant-name">Name Teilnehmer</p>
    <div class="name-rule"></div>

    <p class="tribute-text">Ihr habt mit Begeisterung und Abenteuerlust an unserer gemeinsamen Reise durch Tunesien teilgenommen. Mit eurem Expeditionsmobil habt ihr die Wüste bezwungen, neue Freundschaften geschlossen und die Magie dieses einzigartigen Landes erlebt.</p>

    <div class="thanks-banner">Danke, dass ihr Teil dieser besonderen Tour wart –<br>auf viele weitere Abenteuer!</div>

    <svg class="vehicle-photo" viewBox="0 0 220 220">
      <defs>
        <radialGradient id="campGround" cx="50%" cy="50%" r="50%">
          <stop offset="0%" stop-color="#a08670"/>
          <stop offset="70%" stop-color="#8d7260"/>
          <stop offset="100%" stop-color="#6f5a4d"/>
        </radialGradient>
      </defs>
      <circle cx="110" cy="110" r="110" fill="#ffffff"/>
      <circle cx="110" cy="110" r="104" fill="var(--photo-ring)"/>
      <circle cx="110" cy="110" r="97" fill="url(#campGround)" role="img" aria-label="Luftbild der Fahrzeuge im Kreis aufgestellt"/>
    </svg>

    <p class="event-date">11.20.2024</p>
    <p class="event-address">Lindenweg 8 12345 Musterau</p>
    <div class="sign-rule place"></div>
    <div class="sign-rule signers"></div>
    <p class="sign-label place">Ort und Datum</p>
    <p class="sign-label signers">Jonas &amp; Malte</p>

    <div class="brand">
      <span class="brand-dot"></span>
      <span class="brand-name">Kranichpfad Reisen</span>
    </div>
  </main>
</body>
</html>
```